BWKA (a church) flyer for our locality to advertise us

A double-sided colour A5 flyer that introduces our church to our local community. It should include our logo, and be sympathetic to its colours. It should say who we are, when we meet and talk about what we do. It needs to show our location and how to get to us, where you can park, and how to contact us.
We want it to look modern, bright and inviting. More information can be found at www.bwka-example.org and www.brightkettle-example.org and Facebook bright.kettle.uk

A copy of our previous flyer is attached. Our folks thought it was too dull and emphasised the cafe too much.

Target Market(s)

People within our locality in SE London who may be interested in attending our church, or visiting our cafe, Bright Kettle

Industry/Entity Type

Charity

Font styles to use
Sans Serif

Colors
6b449b
876aae
33a6d7
0455a3
fee18a
ffffff

Requirements
Must have
• A description of who we are at BWKA; what we do; what our values are; when & where we meet & how to contact us. Something to draw people in - a magnetic effect. A modern look & feel. A primary emphasis on our church.
Nice to have
• Design that is sympathetic to our logo colours (livery)
Should not have
• Too much emphasis on the Bright Kettle cafe.

```html
<!DOCTYPE html>
<html lang="en">
<head>
<meta charset="utf-8">
<title>BWKA flyer – front and back</title>
<link rel="stylesheet" href="https://fonts.googleapis.com/css2?family=Lobster&family=Arvo:wght@700&family=Lato:wght@400;700&family=Merriweather:wght@700&display=swap">
<style>
  :root{
    --stage:#2b2a29;
    --brown-deep:#2a1608;
    --brown:#432310;
    --gold:#e9a21c;
    --gold-light:#f6c24a;
    --blue:#3b30d4;
    --orange:#f2a332;
    --peach:#fde1a0;
    --ink:#1c1410;
    --white:#ffffff;
    --cream:#f1e6d8;
    --panel:#1d0f06;
    --navy-head:#2f2bb8;
  }
  *{box-sizing:border-box;margin:0;padding:0}
  html,body{width:1200px;height:888px;overflow:hidden}
  body{background:var(--stage);font-family:'Lato',sans-serif;position:relative}
  .flyer{position:absolute;top:68px;width:528px;height:750px;overflow:hidden;background:var(--brown-deep)}
  .flyer--front{left:52px}
  .flyer--back{left:619px}
  .flyer__art{position:absolute;inset:0;width:528px;height:750px}
  .abs{position:absolute}

  /* front */
  .title-band{left:0;top:16px;width:528px;height:82px;background:rgba(255,255,255,.82)}
  .title{left:0;top:18px;width:528px;text-align:center;font-family:'Lobster',cursive;font-size:37px;color:var(--ink)}
  .tagline{left:0;top:64px;width:528px;text-align:center;font-size:28px;letter-spacing:3.5px;color:var(--blue)}
  .emblem{left:18px;top:207px;width:150px;height:150px;border-radius:50%;background:var(--white);display:flex;align-items:center;justify-content:center;font-weight:700;font-size:28px;color:#5b3d8f}
  .headline{left:14px;top:372px;font-family:'Arvo',serif;font-size:88px;line-height:1;color:var(--gold);letter-spacing:1px}
  .headline-script{left:302px;top:462px;font-family:'Lobster',cursive;font-size:54px;color:var(--white);transform:rotate(-4deg)}
  .welcome{left:0;top:468px;width:278px;height:116px;background:var(--panel);border-radius:0 12px 12px 0;padding:8px 16px;color:var(--white)}
  .welcome h2{font-size:17px;font-weight:700;line-height:1.3}
  .welcome p{font-size:14.5px;line-height:1.22;color:var(--cream)}
  .info{font-size:13.5px;line-height:1.25;color:var(--white)}
  .info b{color:var(--gold-light);font-weight:700}
  .info--left{left:16px;top:596px;width:280px}
  .info--right{right:23px;top:596px;width:240px;text-align:right}
  .info .gap{display:block;height:14px}
  .gold-bar{left:0;bottom:0;width:528px;height:16px;background:linear-gradient(90deg,#b97710,var(--gold-light),#c4820f)}

  /* back */
  .venue{left:25px;top:154px;width:178px;height:178px;border-radius:50%;background:var(--orange);border:3px solid var(--white);display:flex;flex-direction:column;align-items:center;justify-content:center;text-align:center;color:var(--ink);font-size:13.5px;font-weight:700;line-height:1.25}
  .venue h3{font-family:'Merriweather',serif;font-size:17px;color:var(--white)}
  .contact-band{left:0;top:360px;width:528px;height:92px;background:var(--peach);padding:12px 18px;display:flex;gap:20px;font-size:12.5px;line-height:1.32;color:var(--ink)}
  .contact-band h4{font-family:'Merriweather',serif;font-size:13px;color:var(--navy-head);margin-bottom:2px}
  .contact-band .col:first-child{width:222px}
  .cafe-title{left:18px;top:466px;font-family:'Merriweather',serif;font-size:16px;color:var(--gold-light)}
  .cafe-copy{left:18px;top:494px;width:494px;font-size:14.5px;line-height:1.27;color:var(--white);text-align:justify}
  .small{font-size:12.5px;line-height:1.3;color:var(--white)}
  .small b{font-family:'Merriweather',serif;font-size:11.5px;color:var(--gold-light)}
  .small--hours{left:18px;top:612px;width:220px}
  .small--travel{left:253px;top:612px;width:262px}
  .small .gold{color:var(--gold-light)}
</style>
</head>
<body>

<section class="flyer flyer--front">
  <svg class="flyer__art" viewBox="0 0 528 750" aria-hidden="false">
    <defs>
      <linearGradient id="photoTone" x1="0" y1="0" x2="1" y2="1">
        <stop offset="0" stop-color="#8a6a52"/>
        <stop offset=".45" stop-color="#b9b3ab"/>
        <stop offset="1" stop-color="#6e4630"/>
      </linearGradient>
      <radialGradient id="brownGlow" cx=".5" cy=".35" r=".8">
        <stop offset="0" stop-color="#4e2a12"/>
        <stop offset="1" stop-color="#241205"/>
      </radialGradient>
    </defs>
    <rect width="528" height="420" fill="url(#photoTone)" role="img" aria-label="Photo of a tablet showing a bible app beside a cup of coffee on a wooden table"/>
    <path d="M0,244 C120,276 250,321 340,306 C430,291 490,226 528,201 L528,750 L0,750Z" fill="var(--blue)"/>
    <path d="M0,262 C120,294 250,339 340,324 C430,309 490,244 528,219 L528,750 L0,750Z" fill="var(--orange)"/>
    <path d="M0,270 C120,302 250,347 340,332 C430,317 490,252 528,227 L528,750 L0,750Z" fill="url(#brownGlow)"/>
  </svg>
  <div class="abs title-band"></div>
  <h1 class="abs title">Brightwell Kingdom Assembly</h1>
  <p class="abs tagline">A PLACE TO BE LOVED</p>
  <div class="abs emblem">BWKA</div>
  <h2 class="abs headline">WORSHIP</h2>
  <p class="abs headline-script">With us</p>
  <div class="abs welcome">
    <h2>BWKA, a place where everyone is welcome:</h2>
    <p>different ethnicities,<br>ages, social groups, abilities<br>and disabilities, and interests.</p>
  </div>
  <div class="abs info info--left">
    <b>Sunday Services:</b> 10.30am - 12.15pm<br>Children's classes available on Sundays
    <span class="gap"></span>
    <b>We also have</b><br>Ladies Group – 1st Friday of every month (informal, informative and lots of fun!)
  </div>
  <div class="abs info info--right">
    <b>1st &amp; 3rd Wednesday :</b><br>7-8pm Prayer &amp; Study
    <span class="gap"></span><br>
    Night vigil – every quarter, please confirm by phone<br>Counselling – by appointment only
  </div>
  <div class="abs gold-bar"></div>
</section>

<section class="flyer flyer--back">
  <svg class="flyer__art" viewBox="0 0 528 750">
    <defs>
      <radialGradient id="brownGlowBack" cx=".5" cy=".3" r=".8">
        <stop offset="0" stop-color="#4e2a12"/>
        <stop offset="1" stop-color="#241205"/>
      </radialGradient>
    </defs>
    <rect width="528" height="330" fill="#e6e3dc" role="img" aria-label="Street map of the area around the venue with roads, river and a pointer to the church"/>
    <path d="M0,228 C80,270 160,302 250,294 C360,284 450,230 528,200 L528,750 L0,750Z" fill="var(--blue)"/>
    <path d="M0,250 C80,292 160,324 250,316 C360,306 450,252 528,222 L528,750 L0,750Z" fill="var(--orange)"/>
    <path d="M0,257 C80,299 160,331 250,323 C360,313 450,259 528,229 L528,750 L0,750Z" fill="url(#brownGlowBack)"/>
    <line x1="150" y1="215" x2="298" y2="132" stroke="#d41f1f" stroke-width="2"/>
    <path d="M298,132 L286,133 L292,143Z" fill="#d41f1f"/>
  </svg>
  <div class="abs venue">
    <h3>Venue:</h3>
    Brightwell Kingdom Assembly<br>BRIGHT KETTLE<br>Unit 4, Kettle Yard,<br>Hollow Green, SE99 1AA
  </div>
  <div class="abs contact-band">
    <div class="col">
      <h4>Contact Us</h4>
      <b>E-mail:</b> hello@bwka-example.org<br>
      <b>Telephone:</b> INT'l +44 (0)20 7946 0123<br>
      <b>Evenings:</b> INT'L +44(0)20 7946 0456
    </div>
    <div class="col">
      <h4>For further enquiries:</h4>
      <b>Office:</b> Tuesday through Friday 3:00 - 4:00pm<br>
      <b>BWKA Web:</b> www.bwka-example.org<br>
      <b>Cafe web:</b> www.brightkettle-example.org.uk
    </div>
  </div>
  <h3 class="abs cafe-title">Bright Kettle Cafe</h3>
  <p class="abs cafe-copy">We offer world class fair trade premium coffees and teas including herbal and organic. We make a range of sandwiches and paninis to order in our kitchen as well as offering home made soup and home baked cake slices. Our venue has FREE WIFI, built in AV and PA and is also available for private hire.</p>
  <div class="abs small small--hours">
    <b>Cafe Opening Hours:</b><br>Tues - Fri: 10am - 3pm<br><br><br>
    Bright Kettle is a community initiatve sponsored by<br><span class="gold">Brightwell Kingdom Assembly</span>
  </div>
  <div class="abs small small--travel">
    <b>Buses:</b> 104, 186, 207, 268, 315<br>
    <b>Trains:</b> Nearest stations: Hollow Green, Marsh Lane, Eastheath<br>
    Parking FREE car park behind car wash in Cedar Walk Road (Check closing times to avoid lock-in; 2 hour time limits have not been enforced)
  </div>
</section>

</body>
</html>
```